Hvac and insulation company needs good looking business card design

We are hvac and insulation company and looking for a new business cards that look to today standards designs

Target Market(s)

homeowners

Industry/Entity Type

Hvac

Contact Information for Business Card

Name: Dorian Velkova
Home comfort consultant
address: 4827 Marrow Ridge Rd #215 Oakland, CA 94611
office: 888-317-5069
cell: 510-642-1388
Lic.# 458127
Email: dorian@quarry-hvac.com
Web: quarry-hvac.com

Requirements
Must have
• clean and sleek look
Nice to have
• simple with a clean look
Should not have
• to busy business card

```html
<!DOCTYPE html>
<html lang="en">
<head>
<meta charset="utf-8">
<title>Quarry Home Solutions – Business Card</title>
<link href="https://fonts.googleapis.com/css2?family=Encode+Sans+Semi+Condensed:wght@400;500;600&family=Varela+Round&display=swap" rel="stylesheet">
<style>
  :root{
    --stage:#4a4a4c;
    --stage-edge:#2f2f30;
    --card:#ffffff;
    --brand-orange:#f58634;
    --sky:#00aeef;
    --ink:#58595b;
    --rule:#4d4d4f;
    --grey-band-a:#f2f3f3;
    --grey-band-b:#dedfe0;
    --grey-ground:#e1e2e3;
    --grey-scene:linear-gradient(180deg,#b3b4b6,#c2c3c5);
    --warm-band-a:#fde591;
    --warm-band-b:#fbd9b8;
    --warm-ground:#fbdcc0;
    --warm-scene-a:linear-gradient(180deg,#f9a95c,#f6a86e);
    --warm-scene-b:linear-gradient(180deg,#f9b87a,#fac49a);
  }
  *{margin:0;padding:0;box-sizing:border-box}
  html,body{width:1200px;height:1000px;overflow:hidden}
  body{background:var(--stage);border:1px solid var(--stage-edge);position:relative;font-family:"Encode Sans Semi Condensed",sans-serif}
  .card{position:absolute;left:286px;width:631px;background:var(--card);overflow:hidden}
  .card--front{top:92px;height:394px}
  .card--back{top:517px;height:395px}
  .card__bands{position:absolute;inset:0;width:100%;height:100%}
  .corner-scene{position:absolute;bottom:0}
  .card--front .corner-scene--left{left:0;width:61px;height:86px;background:var(--grey-scene)}
  .card--front .corner-scene--right{right:0;width:86px;height:144px;background:var(--grey-scene)}
  .card--back .corner-scene--left{left:0;width:81px;height:116px;background:var(--warm-scene-a)}
  .card--back .corner-scene--right{right:0;width:102px;height:151px;background:var(--warm-scene-b)}
  .brand{position:absolute;left:0;right:0;top:140px;display:flex;align-items:center;justify-content:center;gap:14px}
  .brand__dot{width:30px;height:30px;border-radius:50%;background:var(--brand-orange)}
  .brand__name{font-family:"Varela Round",sans-serif;font-size:40px;color:var(--brand-orange);letter-spacing:0.5px}
  .call-pill{position:absolute;left:217px;top:286px;width:196px;height:39px;border-radius:8px;background:var(--sky);color:#fff;font-size:17px;display:flex;align-items:center;justify-content:center;letter-spacing:0.3px}
  .person{position:absolute;left:0;right:0;top:80px;text-align:center}
  .person__name{font-size:39px;color:var(--sky);font-weight:400;letter-spacing:0.5px;line-height:1}
  .person__name strong{font-weight:600}
  .person__title{font-size:23px;color:var(--ink);margin-top:10px}
  .person__rule{position:absolute;left:165px;top:170px;width:302px;height:2px;background:var(--rule)}
  .contact{position:absolute;left:0;right:0;text-align:center;font-size:17px;color:var(--ink);display:flex;justify-content:center;align-items:center;gap:6px;white-space:nowrap}
  .contact svg{fill:var(--ink);flex:none}
  .contact--address{top:191px}
  .contact--phone{top:220px}
  .contact--web{top:252px}
  .contact__sep{margin:0 12px}
  .contact__gap{width:8px}
</style>
</head>
<body>

<section class="card card--front">
  <svg class="card__bands" viewBox="0 0 631 394" aria-hidden="true">
    <rect x="0" y="0" width="274" height="21" fill="var(--grey-band-a)"/>
    <rect x="274" y="0" width="357" height="21" fill="var(--grey-band-b)"/>
    <rect x="0" y="387" width="631" height="7" fill="var(--grey-ground)"/>
  </svg>
  <div class="corner-scene corner-scene--left" role="img" aria-label="Small grey house illustration"></div>
  <div class="corner-scene corner-scene--right" role="img" aria-label="Grey house illustration"></div>
  <div class="brand">
    <span class="brand__dot"></span>
    <span class="brand__name">quarry home solutions</span>
  </div>
  <div class="call-pill">Call us: 888-317-5069</div>
</section>

<section class="card card--back">
  <svg class="card__bands" viewBox="0 0 631 395" aria-hidden="true">
    <rect x="0" y="0" width="211" height="19" fill="var(--warm-band-a)"/>
    <rect x="211" y="0" width="420" height="19" fill="var(--warm-band-b)"/>
    <rect x="57" y="384" width="574" height="11" fill="var(--warm-ground)"/>
  </svg>
  <div class="corner-scene corner-scene--left" role="img" aria-label="Orange house illustration"></div>
  <div class="corner-scene corner-scene--right" role="img" aria-label="Peach house illustration"></div>
  <div class="person">
    <h1 class="person__name">DORIAN <strong>VELKOVA</strong></h1>
    <p class="person__title">Home comfort consultant</p>
  </div>
  <div class="person__rule"></div>
  <p class="contact contact--address">
    <svg width="12" height="15" viewBox="0 0 12 15"><path d="M6 0a6 6 0 0 0-6 6c0 4.5 6 9 6 9s6-4.5 6-9a6 6 0 0 0-6-6zm0 8.3A2.3 2.3 0 1 1 6 3.7a2.3 2.3 0 0 1 0 4.6z"/></svg>
    <span>4827 Marrow Ridge Rd #215 Oakland, CA 94611</span>
  </p>
  <p class="contact contact--phone">
    <svg width="14" height="14" viewBox="0 0 24 24"><path d="M6.6 10.8a15.1 15.1 0 0 0 6.6 6.6l2.2-2.2c.3-.3.7-.4 1-.2 1.1.4 2.3.6 3.6.6.6 0 1 .4 1 1V20c0 .6-.4 1-1 1A17 17 0 0 1 3 4c0-.6.4-1 1-1h3.5c.6 0 1 .4 1 1 0 1.3.2 2.5.6 3.6.1.3 0 .7-.2 1z"/></svg>
    <span>510-642-1388</span><span class="contact__sep">|</span><span>Lic.# 458127</span>
  </p>
  <p class="contact contact--web">
    <svg width="14" height="11" viewBox="0 0 14 11"><path d="M0 0h14v11H0zm1.2 1.2v.3L7 5.6l5.8-4.1v-.3zm0 1.7v6.9h11.6V2.9L7 7z"/></svg>
    <span>dorian@quarry-hvac.com</span>
    <span class="contact__gap"></span>
    <svg width="14" height="14" viewBox="0 0 14 14"><path d="M7 0a7 7 0 1 0 0 14A7 7 0 0 0 7 0zm4.9 4.5H9.8a9.7 9.7 0 0 0-1-3 5.7 5.7 0 0 1 3.1 3zM7 1.3c.6.9 1.1 2 1.4 3.2H5.6C5.9 3.3 6.4 2.2 7 1.3zM1.5 8.4a5.6 5.6 0 0 1 0-2.8h2.3a11 11 0 0 0 0 2.8zm.6 1.1h2.1c.2 1.1.6 2.1 1 3a5.7 5.7 0 0 1-3.1-3zm2.1-5h-2.1a5.7 5.7 0 0 1 3.1-3c-.4.9-.8 1.900-1 3zM7 12.7c-.6-.9-1.1-2-1.4-3.2h2.8c-.3 1.2-.8 2.3-1.4 3.2zm1.6-4.3H5.4a9.4 9.4 0 0 1 0-2.8h3.2a9.4 9.4 0 0 1 0 2.8zm.2 4.1c.4-.9.8-1.9 1-3h2.1a5.7 5.7 0 0 1-3.1 3zm1.4-4.1a11 11 0 0 0 0-2.8h2.3a5.6 5.6 0 0 1 0 2.8z"/></svg>
    <span>quarry-hvac.com</span>
  </p>
</section>

</body>
</html>
```